New business card for civil engineering company - "Keel Survey"

We need a business card designed for our new structural engineering company.

The company name is "Keel Survey" logo files attached.

We would like the following:
* Two-sided card
* Simple design

Information to be placed on the card:
Name - Marcus Hollby
Job Title - Director / Structural Engineer
Credentials - BEng(Hons), CPEng, CMengNZ, IntPE(NZ)
Email - marcus.hollby@keelsurvey-example.co.nz
mobile - 0219036458
website - www.keelsurvey-example.co.nz

```html
<!DOCTYPE html>
<html lang="en">
<head>
<meta charset="utf-8">
<title>Keel Survey — Business Card</title>
<link href="https://fonts.googleapis.com/css2?family=Rubik:wght@400;500&family=Exo+2:wght@500&display=swap" rel="stylesheet">
<style>
  :root {
    --backdrop: #d8d3cb;
    --card-white: #ffffff;
    --facet-light: #fafafa;
    --facet-mid: #dedede;
    --ink-dark: #3a3a3c;
    --ink-grey: #6b6b6e;
    --band-dark: #4a4a4c;
    --band-light: #e9e9e9;
    --mark-grey: #6f6f72;
    --accent-blue: #3f8fd8;
    --rule: #c4c4c4;
  }
  * { margin: 0; padding: 0; box-sizing: border-box; }
  html, body { width: 900px; height: 1200px; overflow: hidden; }
  body {
    position: relative;
    background: var(--backdrop);
    font-family: "Rubik", Arial, sans-serif;
    color: var(--ink-dark);
  }
  .card {
    position: absolute;
    left: 82px;
    width: 738px;
    height: 430px;
    overflow: hidden;
    box-shadow: 0 6px 18px rgba(0,0,0,0.28);
  }

  /* Front */
  .card-front {
    top: 127px;
    border-radius: 46px 0 46px 0;
  }
  .front-facets {
    position: absolute;
    inset: 0;
    background: radial-gradient(ellipse at 50% 55%, var(--facet-light) 0%, #eeeeee 45%, var(--facet-mid) 100%);
  }
  .front-mark {
    position: absolute;
    left: 340px;
    top: 195px;
    width: 58px;
    height: 58px;
    background: var(--mark-grey);
  }
  .front-name {
    position: absolute;
    left: 0; right: 0;
    top: 277px;
    text-align: center;
  }
  .brand-name {
    font-family: "Exo 2", "Rubik", sans-serif;
    font-weight: 500;
    letter-spacing: 2px;
    text-transform: uppercase;
    color: var(--ink-dark);
    line-height: 1;
  }
  .front-name .brand-name { font-size: 34px; }
  .tagline {
    margin-top: 8px;
    font-size: 12.5px;
    letter-spacing: 2.6px;
    text-transform: uppercase;
    color: var(--ink-dark);
  }
  .web-band {
    position: absolute;
    left: 0; right: 0;
    top: 389px;
    height: 21px;
    background: var(--band-dark);
    color: #f2f2f2;
    font-size: 13px;
    letter-spacing: 8.5px;
    text-align: center;
    line-height: 21px;
    text-transform: uppercase;
  }
  .web-band-foot {
    position: absolute;
    left: 0; right: 0;
    top: 410px;
    height: 20px;
    background: var(--band-light);
  }

  /* Back */
  .card-back {
    top: 635px;
    background: var(--card-white);
    border-radius: 0 56px 0 56px;
  }
  .back-mark {
    position: absolute;
    left: 339px;
    top: 100px;
    width: 60px;
    height: 60px;
    background: var(--accent-blue);
  }
  .back-name {
    position: absolute;
    left: 0; right: 0;
    top: 228px;
    text-align: center;
  }
  .back-name .brand-name { font-size: 29px; }
  .back-name .tagline {
    margin-top: 6px;
    font-size: 11px;
    letter-spacing: 2.5px;
    color: var(--ink-grey);
  }
  .divider {
    position: absolute;
    left: 48px;
    right: 47px;
    top: 295px;
    border-top: 1px solid var(--rule);
  }
  .contact-list {
    position: absolute;
    left: 46px;
    top: 313px;
    list-style: none;
    font-size: 15.5px;
    line-height: 26px;
    color: var(--ink-dark);
  }
  .contact-label {
    display: inline-block;
    width: 44px;
    color: var(--accent-blue);
  }
  .person {
    position: absolute;
    right: 47px;
    top: 313px;
    text-align: right;
    font-size: 16.5px;
    letter-spacing: 0.3px;
    line-height: 24px;
    color: var(--ink-grey);
  }
  .person-name {
    font-size: 21px;
    letter-spacing: 1px;
    color: var(--ink-dark);
    text-transform: uppercase;
    line-height: 28px;
  }
  .person-name strong { font-weight: 500; }
  .person-name span { font-weight: 400; }
</style>
</head>
<body>
  <section class="card card-front">
    <div class="front-facets" role="img" aria-label="Soft grey low-poly faceted background pattern"></div>
    <div class="front-mark"></div>
    <div class="front-name">
      <div class="brand-name">Keel Survey</div>
      <div class="tagline">Peer Review Specialists</div>
    </div>
    <div class="web-band">www.keelsurvey-example.co.nz</div>
    <div class="web-band-foot"></div>
  </section>

  <section class="card card-back">
    <div class="back-mark"></div>
    <div class="back-name">
      <div class="brand-name">Keel Survey</div>
      <div class="tagline">Peer Review Specialists</div>
    </div>
    <div class="divider"></div>
    <ul class="contact-list">
      <li><span class="contact-label">P /</span>0219036458</li>
      <li><span class="contact-label">E /</span>marcus.hollby@keelsurvey-example.co.nz</li>
      <li><span class="contact-label">W /</span>www.keelsurvey-example.co.nz</li>
    </ul>
    <div class="person">
      <div class="person-name"><strong>Marcus</strong> <span>Hollby</span></div>
      <div class="person-title">Director / Structural Engineer</div>
      <div class="person-credentials">BEng(Hons), CPEng, CMengNZ, IntPE(NZ)</div>
    </div>
  </section>
</body>
</html>
```